Real Estate Biz Card

-Card Size: Standard
-Background: Dark grey or black. I am open to gradient or a textured background.
-Other Colors: I dont mind pops of color. Contrasty blue, lime green, red Etc. Feel free to get creative.
-Text color: be creative
-Font: I like modern styles. Something that works well with my KV718 logo. See attached
-I would like my logo (KV718) watermarked on the card. Either on one side or both.
-Front of Card: keep it simple. Head shot, name, Logo, Phone #
-Back: add the rest of the details. See list below.
-brokerages logo as well as the Domivest and Equal Housing Opportunity logos on the card
-Name: Tod Marwick
-Residential Real Estate
-Cell:
-Email:
-Site:
-Office Address:
-very small/fine print "Each office independently owned & operated

```html
<!DOCTYPE html>
<html lang="en">
<head>
<meta charset="utf-8">
<title>KV718 Business Card</title>
<link href="https://fonts.googleapis.com/css2?family=Open+Sans:wght@400;600;700;800&display=swap" rel="stylesheet">
<style>
  :root {
    --page: #e4e6e9;
    --brand-blue: #1f76c6;
    --card-dark: #25272a;
    --ink-dark: #2a2d31;
    --stripe-grey: #8a8d92;
    --text-light: #f2f3f5;
    --text-muted: #a7abb1;
    --photo-top: #d9dbde;
    --photo-bottom: #b4b8be;
  }
  * { margin: 0; padding: 0; box-sizing: border-box; }
  html, body { width: 1200px; height: 900px; overflow: hidden; }
  body {
    background: var(--page);
    font-family: "Open Sans", Arial, sans-serif;
    position: relative;
  }
  .card {
    position: absolute;
    left: 250px;
    width: 700px;
    height: 400px;
    overflow: hidden;
    box-shadow: 0 6px 18px rgba(0,0,0,.18);
  }
  .card-back { top: 35px; background: var(--brand-blue); }
  .card-front { top: 465px; background: var(--card-dark); }

  /* Back side */
  .wordmark-large {
    position: absolute; left: 0; right: 0; top: 120px;
    display: flex; justify-content: center; align-items: center; gap: 16px;
  }
  .wordmark-large .name {
    font-weight: 800; font-size: 96px; letter-spacing: 4px; color: var(--ink-dark); line-height: 1;
  }
  .wordmark-large .mark { width: 26px; height: 26px; background: var(--ink-dark); }
  .affiliations {
    position: absolute; left: 0; right: 0; top: 290px;
    display: flex; justify-content: center; align-items: center; gap: 22px;
  }
  .badge { width: 28px; height: 30px; border: 3px solid var(--ink-dark); }
  .brokerage {
    font-weight: 700; font-size: 17px; color: var(--ink-dark); letter-spacing: .5px;
  }

  /* Front side */
  .fold { position: absolute; inset: 0; }
  .wordmark {
    position: absolute; left: 58px; top: 120px;
    display: flex; align-items: center; gap: 10px;
  }
  .wordmark .name {
    font-weight: 800; font-size: 64px; letter-spacing: 3px; color: var(--brand-blue); line-height: 1;
  }
  .wordmark .mark { width: 16px; height: 16px; background: var(--brand-blue); }
  .contact {
    position: absolute; left: 100px; top: 212px;
    color: var(--text-light); font-size: 15px; line-height: 21px;
  }
  .contact li { list-style: none; display: flex; align-items: center; gap: 8px; }
  .contact svg { width: 14px; height: 14px; fill: var(--brand-blue); flex: none; }
  .contact .fine { font-size: 9px; line-height: 16px; color: var(--text-light); }
  .headshot {
    position: absolute; left: 450px; top: 40px; width: 185px; height: 140px;
    border-radius: 14px;
    background: linear-gradient(180deg, var(--photo-top), var(--photo-bottom));
  }
  .agent {
    position: absolute; left: 430px; top: 188px; width: 225px; text-align: center;
  }
  .agent .agent-name {
    font-weight: 700; font-size: 15px; color: var(--brand-blue); text-transform: uppercase; letter-spacing: .5px;
  }
  .agent .agent-role { font-size: 15px; color: var(--text-muted); }
  .site {
    position: absolute; left: 480px; top: 318px;
    transform: rotate(-8deg); transform-origin: left top;
    font-size: 15px; font-weight: 600; letter-spacing: 5px; color: var(--ink-dark);
  }
</style>
</head>
<body>

<section class="card card-back" aria-label="Card back">
  <div class="wordmark-large">
    <span class="mark"></span>
    <span class="name">KV718</span>
  </div>
  <div class="affiliations">
    <span class="badge" aria-label="Domivest badge"></span>
    <span class="badge" aria-label="Equal housing badge"></span>
    <span class="brokerage">Northgate Realty</span>
  </div>
</section>

<section class="card card-front" aria-label="Card front">
  <svg class="fold" viewBox="0 0 700 400" aria-hidden="true">
    <polygon points="160,400 440,290 700,250 700,266 444,306 190,400" fill="var(--stripe-grey)"/>
    <polygon points="190,400 444,306 700,266 700,400" fill="var(--brand-blue)"/>
  </svg>

  <div class="wordmark">
    <span class="name">KV718</span>
    <span class="mark"></span>
  </div>

  <ul class="contact">
    <li>4120 Alder Court</li>
    <li>Fairview, Oregon 97024</li>
    <li>
      <svg viewBox="0 0 24 24"><path d="M6.6 10.8a15.2 15.2 0 0 0 6.6 6.6l2.2-2.2a1 1 0 0 1 1-.25 11.4 11.4 0 0 0 3.6.57 1 1 0 0 1 1 1V20a1 1 0 0 1-1 1A17 17 0 0 1 3 4a1 1 0 0 1 1-1h3.5a1 1 0 0 1 1 1c0 1.25.2 2.45.57 3.57a1 1 0 0 1-.25 1z"/></svg>
      555 214 7630
    </li>
    <li>
      <svg viewBox="0 0 24 24"><path d="M7 1h10a2 2 0 0 1 2 2v18a2 2 0 0 1-2 2H7a2 2 0 0 1-2-2V3a2 2 0 0 1 2-2zm0 3v14h10V4zm5 15.5a1 1 0 1 0 0 2 1 1 0 0 0 0-2z"/></svg>
      555 309 4471
    </li>
    <li>
      <svg viewBox="0 0 24 24"><path d="M2 5h20v14H2zm2 2v.5l8 5 8-5V7l-8 5z"/></svg>
      tod@kv718.com
    </li>
    <li class="fine">Each office independently owned &amp; operated</li>
  </ul>

  <div class="headshot" role="img" aria-label="Agent headshot photo"></div>
  <div class="agent">
    <div class="agent-name">Tod Marwick</div>
    <div class="agent-role">Residential Real Estate</div>
  </div>

  <div class="site">www.kv718.com</div>
</section>

</body>
</html>
```